R & T Summit Construction Business Card ideas

We want a business card to represents our company in a way that looks professional but is also a business card that is unique!

Industry/Entity Type

Construction Company

Contact Information for Business Card

open to all design ideas, just want to be able to see different options to choose from in either color or grayscale.

Requirements
Must have
• Our names and phone numbers
• Mark Hollis 386-555-0142
• Derek Walsh 386-555-0187
• Business logo

```html
<!DOCTYPE html>
<html lang="en">
<head>
<meta charset="utf-8">
<title>R &amp; T Summit Construction — Business Card</title>
<link rel="stylesheet" href="https://fonts.googleapis.com/css2?family=Cinzel:wght@600&display=swap">
<style>
  :root {
    --backdrop: #e7e4df;
    --card-white: #ffffff;
    --card-ink: #111111;
    --band-black: #0d0d0d;
    --band-grey: #a9a9a9;
    --text-light: #f2f2f2;
    --shadow: rgba(0, 0, 0, 0.18);
  }
  * { box-sizing: border-box; margin: 0; padding: 0; }
  html, body {
    width: 1200px;
    height: 1022px;
    overflow: hidden;
    background: var(--backdrop);
  }
  .sheet {
    width: 1200px;
    height: 1022px;
    display: flex;
    flex-direction: column;
    align-items: center;
    justify-content: center;
    gap: 60px;
  }
  .card {
    position: relative;
    width: 700px;
    height: 400px;
    border-radius: 18px;
    overflow: hidden;
    background: var(--card-white);
    box-shadow: 0 10px 30px var(--shadow);
  }
  .card-band {
    position: absolute;
    inset: 0;
    width: 100%;
    height: 100%;
  }
  .band-grey { fill: var(--band-grey); }
  .band-black { fill: var(--band-black); }

  .company-name {
    position: absolute;
    font-family: "Cinzel", serif;
    font-weight: 600;
    color: var(--card-ink);
    letter-spacing: 0.04em;
    display: flex;
    align-items: center;
    gap: 14px;
  }
  .company-name .mark-square {
    width: 18px;
    height: 18px;
    background: var(--card-ink);
    flex: none;
  }
  .card-front .company-name {
    left: 70px;
    top: 92px;
    font-size: 34px;
  }
  .card-back .company-name {
    left: 0;
    right: 0;
    top: 0;
    bottom: 0;
    justify-content: center;
    font-size: 36px;
  }

  .contacts {
    position: absolute;
    left: 60px;
    bottom: 34px;
    font-family: "Cinzel", serif;
    font-weight: 600;
    color: var(--text-light);
    list-style: none;
  }
  .contact-name {
    font-size: 21px;
    letter-spacing: 0.08em;
    line-height: 1.15;
  }
  .contact-phone {
    display: flex;
    align-items: center;
    gap: 8px;
    font-size: 19px;
    letter-spacing: 0.06em;
    line-height: 1.2;
    margin-bottom: 6px;
  }
  .phone-icon {
    width: 14px;
    height: 14px;
    fill: var(--text-light);
    flex: none;
  }
</style>
</head>
<body>
<main class="sheet">
  <section class="card card-front" aria-label="Business card front">
    <svg class="card-band" viewBox="0 0 700 400" preserveAspectRatio="none" aria-hidden="true">
      <path class="band-grey" d="M0,196 C230,196 470,290 700,350 L700,400 L0,400 Z"/>
      <path class="band-black" d="M0,226 C230,226 470,318 700,372 L700,400 L0,400 Z"/>
    </svg>

    <div class="company-name"><span class="mark-square"></span>R &amp; T Summit Construction</div>

    <ul class="contacts">
      <li class="contact-name">Mark Hollis</li>
      <li class="contact-phone">
        <svg class="phone-icon" viewBox="0 0 24 24" aria-hidden="true"><path d="M6.6 10.8a15.1 15.1 0 0 0 6.6 6.6l2.2-2.2c.3-.3.7-.4 1-.2 1.1.4 2.3.6 3.6.6.6 0 1 .4 1 1V20c0 .6-.4 1-1 1A17 17 0 0 1 3 4c0-.6.4-1 1-1h3.5c.6 0 1 .4 1 1 0 1.3.2 2.5.6 3.6.1.3 0 .7-.2 1z"/></svg>
        386-555-0142
      </li>
      <li class="contact-name">Derek Walsh</li>
      <li class="contact-phone">
        <svg class="phone-icon" viewBox="0 0 24 24" aria-hidden="true"><path d="M6.6 10.8a15.1 15.1 0 0 0 6.6 6.6l2.2-2.2c.3-.3.7-.4 1-.2 1.1.4 2.3.6 3.6.6.6 0 1 .4 1 1V20c0 .6-.4 1-1 1A17 17 0 0 1 3 4c0-.6.4-1 1-1h3.5c.6 0 1 .4 1 1 0 1.3.2 2.5.6 3.6.1.3 0 .7-.2 1z"/></svg>
        386-555-0187
      </li>
    </ul>
  </section>

  <section class="card card-back" aria-label="Business card back">
    <div class="company-name"><span class="mark-square"></span>R &amp; T Summit Construction</div>
  </section>
</main>
</body>
</html>
```